Northern Horizons Published Photographer Website

I need a website to feature a home page slide show of 6 of my top photos then a few simple pages including; gallery, bio, social, checkout, services

Target Market(s)

photography

Industry/Entity Type

Photographer

Coding

Coded - Design and coding required

Number of Pages Required

5+ page

Colors

Designer to choose colors to be used in the design.

Requirements
Must have
• clean eye catching elegant trendy
Nice to have
• unique and creative from other photographer websites

```html
<!DOCTYPE html>
<html lang="en">
<head>
<meta charset="utf-8">
<title>Northern Horizons Photography</title>
<link rel="stylesheet" href="https://fonts.googleapis.com/css2?family=Questrial&family=Montserrat:wght@500;600;700&display=swap">
<style>
:root{
  --gold:#f5b300;
  --gold-deep:#c9930a;
  --ink:#000000;
  --stone:#dcd8d7;
  --paper:#ffffff;
  --muted:#8a8a8a;
  --text:#1a1a1a;
}
*{box-sizing:border-box;margin:0;padding:0}
html,body{width:1200px;height:4122px;overflow:hidden}
body{position:relative;background:var(--stone);font-family:"Questrial",sans-serif;color:var(--text)}
.abs{position:absolute}

/* hero */
.hero{left:0;top:0;width:1200px;height:694px;background:var(--ink)}
.hero-art{left:0;top:0;width:1200px;height:893px}
.nav{left:70px;top:48px;display:flex;gap:0;font-size:17px;letter-spacing:.3px}
.nav a{color:var(--paper);text-decoration:none;position:absolute;white-space:nowrap}
.nav a.is-active{color:var(--gold)}
.brand-badge{left:888px;top:27px;width:237px;height:75px;background:var(--ink);display:flex;align-items:center;justify-content:center;color:var(--paper);font-size:20px}
.brand-main{left:109px;top:252px;color:var(--paper);font-size:52px;white-space:nowrap;display:flex;align-items:center;gap:18px}
.brand-main .mark{width:26px;height:26px;border-radius:50%;background:var(--paper)}
.btn{display:flex;align-items:center;justify-content:center;background:var(--gold);color:var(--paper);font-family:"Montserrat",sans-serif;font-weight:700}
.btn-contact{left:189px;top:461px;width:232px;height:67px;font-size:25px}
.dots{display:flex;align-items:center;justify-content:center;gap:14px;border:2px solid var(--gold);border-radius:10px}
.dots span{width:12px;height:12px;border-radius:50%;border:2px solid var(--gold)}
.dots span.on{background:var(--gold)}

/* slider */
.slider-band{left:0;top:894px;width:1200px;height:504px;background:linear-gradient(90deg,#3f6f6b 0%,#9a5a2a 30%,#4a7774 55%,#b8672c 80%,#4a7270 100%)}
.slide{background:#ccc}
.slide-left{left:0;top:962px;width:226px;height:483px;background:linear-gradient(160deg,#2a64c8 0%,#f3a53a 55%,#6e4a3a 100%)}
.slide-main{left:275px;top:962px;width:655px;height:486px;background:linear-gradient(180deg,#6fc1bd 0%,#e2a455 35%,#c9782c 55%,#e7a44a 70%,#6cbab6 100%);box-shadow:0 2px 6px rgba(0,0,0,.35)}
.slide-right{left:974px;top:962px;width:226px;height:483px;background:linear-gradient(180deg,#e35a18 0%,#7c8fae 30%,#c7783a 65%,#b4421a 100%)}

/* headings */
.heading{left:0;width:1200px;text-align:center}
.heading .lead{display:block;color:var(--text);font-size:58px;line-height:1}
.heading .big{display:block;color:var(--gold);font-size:78px;line-height:1;letter-spacing:1px}
.divider{height:24px}

.about-copy{left:240px;top:1818px;width:720px;text-align:center;color:var(--muted);font-size:17px;line-height:21px}
.about-copy p+p{margin-top:20px}
.btn-more{left:510px;top:2045px;width:164px;height:48px;font-size:18px}

/* clients */
.clients{left:0;top:2232px;width:1200px;height:880px;background:var(--paper)}
.texture-top{left:0;top:2232px;width:1200px;height:60px;background:linear-gradient(180deg,#d9d9d9,#ffffff)}
.texture-bottom{left:0;top:3060px;width:1200px;height:52px;background:linear-gradient(180deg,#ffffff,#d9d9d9)}
.oval{width:248px;height:335px;border-radius:50%;border:3px solid #f3e2b4;overflow:hidden}
.oval-1{left:188px;top:2555px;background:linear-gradient(160deg,#b5891a,#8c6a12)}
.oval-2{left:477px;top:2555px;background:linear-gradient(180deg,#f2b6b8,#eba7aa)}
.oval-3{left:766px;top:2555px;background:linear-gradient(180deg,#2a2f34,#1b1e22)}
.client-name{left:188px;top:2690px;width:248px;text-align:center;color:var(--paper);font-family:"Montserrat",sans-serif;font-weight:600;font-size:28px}
.client-stars{left:188px;top:2727px;width:248px;display:flex;justify-content:center;gap:4px}
.arrow{width:30px;height:70px}

/* footer */
.contact{left:0;top:3216px;width:1200px;height:906px;background:var(--ink)}
.contact-photo{left:59px;top:3373px;width:541px;height:590px;background:linear-gradient(160deg,#6a7a3a 0%,#c8a24a 35%,#b98c66 60%,#4e5a32 100%)}
.contact-head{left:664px;top:3458px;color:var(--paper)}
.contact-head .lead{display:block;font-size:54px;line-height:1}
.contact-head .big{display:block;color:var(--gold);font-family:"Montserrat",sans-serif;font-weight:700;font-size:59px;line-height:1;margin-top:14px}
.info{left:676px;color:var(--paper);font-size:17px;display:flex;align-items:center;gap:14px}
.info svg{flex:none}
.follow{left:677px;top:3838px;color:var(--paper);font-size:25px;display:flex;align-items:center;gap:14px}
.follow .social{width:22px;height:22px;background:var(--gold);border-radius:3px}
.footer-rule{left:0;top:4024px;width:1200px;height:1px;background:#6b5410}
.copyright{left:0;top:4055px;width:1200px;text-align:center;color:var(--paper);font-size:16px}
.copyright em{font-style:normal;color:var(--gold)}
</style>
</head>
<body>

<section class="abs hero"></section>

<svg class="abs hero-art" viewBox="0 0 1200 893" role="img" aria-label="Diamond-cut collage of landscape photographs: a bridge in mist, autumn trees, a river and a stone wall">
  <defs>
    <linearGradient id="trees" x1="0" y1="0" x2="1" y2="1">
      <stop offset="0" stop-color="#9aa06a"/><stop offset=".5" stop-color="#b08a2a"/><stop offset="1" stop-color="#4d5a2a"/>
    </linearGradient>
    <linearGradient id="mist" x1="0" y1="0" x2="0" y2="1">
      <stop offset="0" stop-color="#e4e6e8"/><stop offset="1" stop-color="#8a8f90"/>
    </linearGradient>
    <linearGradient id="rock" x1="0" y1="0" x2="1" y2="1">
      <stop offset="0" stop-color="#9a9588"/><stop offset="1" stop-color="#3a3832"/>
    </linearGradient>
  </defs>
  <polygon points="660,0 1200,0 1200,893 1060,780 720,440 900,260" fill="url(#trees)"/>
  <polygon points="541,272 728,125 840,250 688,413" fill="url(#mist)"/>
  <polygon points="700,430 840,290 960,410 820,560" fill="#7f8a5e"/>
  <polygon points="1050,715 1200,600 1200,893" fill="url(#rock)"/>
  <g fill="#000">
    <polygon points="655,0 690,0 530,140 515,120"/>
    <polygon points="840,250 860,268 700,430 680,413"/>
    <polygon points="1000,120 1020,140 740,420 720,400"/>
    <polygon points="1200,130 1200,170 860,510 840,490"/>
    <polygon points="1200,380 1200,420 1000,620 980,600"/>
    <polygon points="1200,570 1200,600 1050,715 1030,700"/>
    <polygon points="960,410 980,430 840,570 820,555"/>
  </g>
</svg>

<nav class="abs nav" aria-label="Main">
  <a class="is-active" style="left:0">HOME</a>
  <a style="left:84px">GALLERY</a>
  <a style="left:194px">BIO</a>
  <a style="left:255px">SOCIAL</a>
  <a style="left:351px">CHECKOUT</a>
  <a style="left:477px">SERVICES</a>
</nav>

<div class="abs brand-badge">Northern Horizons</div>

<div class="abs brand-main">Northern Horizons<span class="mark"></span></div>

<a class="abs btn btn-contact">CONTACT ME</a>

<div class="abs dots" style="left:749px;top:624px;width:115px;height:34px"><span class="on"></span><span></span><span></span></div>

<!-- slider -->
<div class="abs slider-band" role="img" aria-label="Blurred backdrop of the featured desert photograph"></div>
<div class="abs slide slide-left" role="img" aria-label="Photograph of a rock arch at sunrise"></div>
<div class="abs slide slide-main" role="img" aria-label="Photograph of a sandstone butte reflected in a lake"></div>
<div class="abs slide slide-right" role="img" aria-label="Photograph of a glass sphere on red rock at sunset"></div>
<div class="abs dots" style="left:534px;top:1475px;width:117px;height:34px"><span class="on"></span><span></span><span></span></div>

<!-- about -->
<h2 class="abs heading" style="top:1612px;font-weight:400"><span class="lead">About</span><span class="big">PHOTOGRAPHY</span></h2>
<svg class="abs divider" style="left:381px;top:1750px" width="416" height="24" viewBox="0 0 416 24" aria-hidden="true">
  <line x1="0" y1="12" x2="186" y2="12" stroke="#f5b300" stroke-width="2"/>
  <line x1="230" y1="12" x2="416" y2="12" stroke="#f5b300" stroke-width="2"/>
  <rect x="195" y="5" width="26" height="16" rx="2" fill="none" stroke="#f5b300" stroke-width="1.6"/>
  <rect x="200" y="2" width="8" height="4" fill="#f5b300"/>
  <circle cx="208" cy="13" r="5" fill="none" stroke="#f5b300" stroke-width="1.6"/>
</svg>
<div class="abs about-copy">
  <p>Lorem ipsum dolor sit amet, consectetur adipisicing elit. Quas aut quidem numquam! Molestias nisi odio itaque eaque vitae dolorem ipsum a, exercitationem laboriosam in quibusdam debitis sequi impedit quia officiis, esse ut fuga doloribus voluptas magnam quasi quo atque dolorum.</p>
  <p>Lorem ipsum dolor sit amet, consectetur adipisicing elit. Quas aut quidem numquam! Molestias nisi odio itaque eaque vitae dolorem ipsum a, exercitationem laboriosam in quibusdam debitis sequi impedit quia officiis, esse ut fuga doloribus voluptas magnam quasi quo atque dolorum.</p>
</div>
<a class="abs btn btn-more">READ MORE</a>

<!-- clients -->
<section class="abs clients"></section>
<div class="abs texture-top"></div>
<div class="abs texture-bottom"></div>
<h2 class="abs heading" style="top:2334px;font-weight:400"><span class="lead" style="font-size:54px">Our Satisfied</span><span class="big" style="font-size:76px">CLIENTS</span></h2>
<svg class="abs divider" style="left:464px;top:2470px" width="264" height="24" viewBox="0 0 264 24" aria-hidden="true">
  <line x1="0" y1="12" x2="110" y2="12" stroke="#f5b300" stroke-width="2"/>
  <line x1="154" y1="12" x2="264" y2="12" stroke="#f5b300" stroke-width="2"/>
  <rect x="119" y="5" width="26" height="16" rx="2" fill="none" stroke="#f5b300" stroke-width="1.6"/>
  <rect x="124" y="2" width="8" height="4" fill="#f5b300"/>
  <circle cx="132" cy="13" r="5" fill="none" stroke="#f5b300" stroke-width="1.6"/>
</svg>
<svg class="abs arrow" style="left:104px;top:2680px" viewBox="0 0 30 70" aria-hidden="true"><polyline points="24,4 6,35 24,66" fill="none" stroke="#f5b300" stroke-width="6"/></svg>
<div class="abs oval oval-1" role="img" aria-label="Portrait of client Jessica with a gold overlay"></div>
<div class="abs oval oval-2" role="img" aria-label="Portrait of a client on a pink backdrop"></div>
<div class="abs oval oval-3" role="img" aria-label="Portrait of a client on a dark backdrop"></div>
<div class="abs client-name">JESSICA</div>
<svg class="abs client-stars" height="20" viewBox="0 0 248 20" aria-label="Four of five stars">
  <g transform="translate(66,0)">
    <polygon points="9,0 11.5,7 19,7 13,11.5 15,19 9,14.5 3,19 5,11.5 -1,7 6.5,7" fill="#fff"/>
    <polygon transform="translate(24,0)" points="9,0 11.5,7 19,7 13,11.5 15,19 9,14.5 3,19 5,11.5 -1,7 6.5,7" fill="#fff"/>
    <polygon transform="translate(48,0)" points="9,0 11.5,7 19,7 13,11.5 15,19 9,14.5 3,19 5,11.5 -1,7 6.5,7" fill="#fff"/>
    <polygon transform="translate(72,0)" points="9,0 11.5,7 19,7 13,11.5 15,19 9,14.5 3,19 5,11.5 -1,7 6.5,7" fill="#fff"/>
    <polygon transform="translate(96,0)" points="9,0 11.5,7 19,7 13,11.5 15,19 9,14.5 3,19 5,11.5 -1,7 6.5,7" fill="#000"/>
  </g>
</svg>
<svg class="abs arrow" style="left:1066px;top:2680px" viewBox="0 0 30 70" aria-hidden="true"><polyline points="6,4 24,35 6,66" fill="none" stroke="#f5b300" stroke-width="6"/></svg>
<div class="abs dots" style="left:542px;top:2963px;width:116px;height:32px"><span class="on"></span><span></span><span></span></div>

<!-- contact -->
<footer class="abs contact"></footer>
<div class="abs contact-photo" role="img" aria-label="Photograph of a photographer in a sun hat with a camera in a sunflower field"></div>
<h2 class="abs contact-head" style="font-weight:400"><span class="lead">Let’s</span><span class="big">CONTACT US</span></h2>
<svg class="abs divider" style="left:704px;top:3593px" width="264" height="24" viewBox="0 0 264 24" aria-hidden="true">
  <line x1="0" y1="12" x2="110" y2="12" stroke="#f5b300" stroke-width="2"/>
  <line x1="154" y1="12" x2="264" y2="12" stroke="#f5b300" stroke-width="2"/>
  <rect x="119" y="5" width="26" height="16" rx="2" fill="none" stroke="#f5b300" stroke-width="1.6"/>
  <rect x="124" y="2" width="8" height="4" fill="#f5b300"/>
  <circle cx="132" cy="13" r="5" fill="none" stroke="#f5b300" stroke-width="1.6"/>
</svg>
<div class="abs info" style="top:3698px">
  <svg width="18" height="18" viewBox="0 0 24 24" aria-hidden="true"><path d="M6.6 10.8a15 15 0 0 0 6.6 6.6l2.2-2.2a1 1 0 0 1 1-.25 11.4 11.4 0 0 0 3.6.6 1 1 0 0 1 1 1V20a1 1 0 0 1-1 1A17 17 0 0 1 3 4a1 1 0 0 1 1-1h3.5a1 1 0 0 1 1 1c0 1.25.2 2.45.6 3.6a1 1 0 0 1-.25 1z" fill="#f5b300"/></svg>
  <span>+0 123 456 7890</span>
</div>
<div class="abs info" style="top:3728px">
  <svg width="18" height="18" viewBox="0 0 24 24" aria-hidden="true"><path d="M6.6 10.8a15 15 0 0 0 6.6 6.6l2.2-2.2a1 1 0 0 1 1-.25 11.4 11.4 0 0 0 3.6.6 1 1 0 0 1 1 1V20a1 1 0 0 1-1 1A17 17 0 0 1 3 4a1 1 0 0 1 1-1h3.5a1 1 0 0 1 1 1c0 1.25.2 2.45.6 3.6a1 1 0 0 1-.25 1z" fill="#f5b300"/></svg>
  <span>+0 123 456 7890</span>
</div>
<div class="abs info" style="top:3773px">
  <svg width="20" height="16" viewBox="0 0 20 16" aria-hidden="true"><rect x="1" y="1" width="18" height="14" fill="none" stroke="#f5b300" stroke-width="1.6"/><polyline points="1,1 10,9 19,1" fill="none" stroke="#f5b300" stroke-width="1.6"/></svg>
  <span>yourname@mail.com</span>
</div>
<div class="abs follow">
  <span>Follow Us :-</span>
  <span class="social" role="img" aria-label="Social profile"></span>
  <span class="social" role="img" aria-label="Social profile"></span>
</div>
<div class="abs footer-rule"></div>
<p class="abs copyright">Copyrights <em>© Northern Horizons Photography</em>. All Rights Reserved.</p>

</body>
</html>
```